COMMERCIAL REAL ESTATE FLYER TEMPLATE

We need a template flyer designed that we can use for a current commercial real estate listing and subsequently use as a template for future listings. We have uploaded images and files to provide an example of an older flyer template we have used. If you have questions or would like to discuss, please contact us at Marty@TLVKE.com. Colors selected should be in line with our attached business card and logo design. Output should be 8.5" X 11".

Target Market(s)

Commercial Real Estate. NO RESIDENTIAL. Needs to have a professional commercial presentation with no reference to residential real estate.

Industry/Entity Type

Real Estate Agent

Font styles to use
Serif

Colors

Designer to choose colors to be used in the design.

Requirements
Must have
• MUST BE SAVED AND ADJUSTABLE IN ONE OF THE FOLLOWING FORMATES: MICROSOFT POWERPOINT, PUBLISHER OR WORD. THIS IS IMPORTANT SO OUR TEAM CAN EASILLY UPDATE TEMPLATE IN READILLY AVAILABLE PROGRAMS THAT ARE SIMPLE FOR TEAM MEMBERS TO USE.
Nice to have
• Needs to have first page template with header and footer displaying our logo, address, phone, email address and contact information for the listing agent. There need to be placeholders that can be easily adjusted based on specific listings. Placeholders will be used for pictures or aerials as the case requires. Needs to have a second page that has header and footer with a clean open block in the middle of the page so agents can customize with site specific details.
Should not have
• There should be no reference to residential. We are a commercial real estate organization that does not do any residential.

```html
<!DOCTYPE html>
<html lang="en">
<head>
<meta charset="utf-8">
<title>Flex Industrial Flyer</title>
<link href="https://fonts.googleapis.com/css2?family=Lato:wght@400;700;900&display=swap" rel="stylesheet">
<style>
:root{
  --navy:#0d1a2e;
  --red:#b81f2b;
  --steel:#6a93bd;
  --paper:#ffffff;
  --panel:#e7e8ea;
  --ink:#3a3d42;
  --cyan:#12b3d6;
}
*{box-sizing:border-box;margin:0;padding:0}
html,body{width:902px;height:1200px;overflow:hidden;background:var(--paper)}
body{font-family:"Lato",sans-serif;color:var(--ink)}
.flyer{position:relative;width:902px;height:1200px;background:var(--paper);overflow:hidden}

.header{position:absolute;left:0;top:0;width:902px;height:146px;background:var(--navy)}
.header-tick{position:absolute;left:23px;top:0;width:146px;height:4px;background:var(--red)}
.brand{position:absolute;background:var(--red);color:#fff;display:flex;flex-direction:column;align-items:center;justify-content:center;text-align:center;font-weight:900;line-height:1.1}
.header .brand{left:55px;top:24px;width:146px;height:112px;font-size:15px;letter-spacing:.5px}
.brand small{display:block;font-size:8px;font-weight:700;margin-top:4px;letter-spacing:.3px}
.contact{position:absolute;color:#fff;font-weight:700;line-height:1.3}
.header .contact{left:230px;top:40px;font-size:15px}
.header-accent{position:absolute;right:60px;top:0;width:300px;height:146px;background:linear-gradient(200deg,var(--navy) 20%,#3a6d8a 65%,var(--cyan) 100%)}
.rule-white{position:absolute;left:0;top:146px;width:902px;height:6px;background:#fff}

.title-band{position:absolute;left:0;top:152px;width:870px;height:104px;background:var(--red);color:#fff;padding:34px 0 0 80px;font-weight:900;font-size:21px;line-height:1.22;letter-spacing:.2px}
.side-strip{position:absolute;right:0;top:152px;width:32px;height:904px;background:var(--steel)}

.body-panel{position:absolute;left:0;top:256px;width:870px;height:800px;background:linear-gradient(100deg,var(--panel) 0%,#fdfdfd 55%,var(--panel) 100%)}
.photo{position:absolute}
.photo-main{left:47px;top:20px;width:524px;height:354px;background:linear-gradient(170deg,#e7e2cf 0%,#b7a37e 45%,#a7764a 70%,#c8b79b 100%)}
.photo-office{left:583px;top:20px;width:256px;height:172px;background:linear-gradient(170deg,#e3e0cf 0%,#8d7656 55%,#6b4a32 100%)}
.photo-lounge{left:583px;top:204px;width:256px;height:170px;background:linear-gradient(170deg,#d8d3bf 0%,#9e8a6c 55%,#7c5f4b 100%)}

.tag{position:absolute;height:27px;background:var(--red);color:#fff;font-weight:900;font-size:14px;display:flex;align-items:center;justify-content:center;letter-spacing:.3px}
.tag-size{left:0;top:397px;width:255px}
.tag-util{left:260px;top:397px;width:262px}
.tag-detention{left:540px;top:397px;width:330px}
.tag-location{left:0;top:669px;width:292px}

.copy{position:absolute;font-size:11px;line-height:1.28;text-align:justify}
.copy-size{left:47px;top:446px;width:193px}
.copy-detention{left:583px;top:446px;width:254px}
.copy-location{left:47px;top:716px;width:800px;text-align:left}
.bullets{position:absolute;left:273px;top:446px;width:240px;list-style:none;font-size:11px;line-height:1.28}
.bullets li{position:relative;padding-left:22px;margin-bottom:9px;text-align:justify}
.bullets li::before{content:"";position:absolute;left:0;top:3px;width:10px;height:10px;border-radius:50%;background:var(--red)}

.footer-rule{position:absolute;left:0;top:1056px;width:902px;height:5px;background:var(--red)}
.footer-gap{position:absolute;left:0;top:1061px;width:902px;height:4px;background:#fff}
.footer{position:absolute;left:0;top:1065px;width:902px;height:135px;background:var(--navy)}
.footer .brand{left:55px;top:30px;width:88px;height:70px;font-size:10px}
.footer .brand small{font-size:5.5px}
.footer .contact{left:160px;top:30px;font-size:14px}
.disclaimer{position:absolute;left:433px;top:28px;width:430px;color:#fff;font-size:9.2px;line-height:1.3}
</style>
</head>
<body>
<main class="flyer">
  <header class="header">
    <div class="header-tick"></div>
    <div class="brand">LOWELL VANCE<small>COMMERCIAL REAL ESTATE</small></div>
    <div class="contact">
      Martin T. Lowell President | CEO<br>
      Phone: (555) 014-2290<br>
      E-Mail: Marty@TLVKE.com<br>
      TREC Broker License: 4417380
    </div>
    <div class="header-accent" role="img" aria-label="Decorative pattern of blue, white and grey squares"></div>
  </header>
  <div class="rule-white"></div>

  <h1 class="title-band">
    FLEX INDUSTRIAL FOR SALE OR LEASE - HOUSTON, TEXAS 4810<br>
    Foundry Park Dr., Houston, Texas 77099
  </h1>
  <div class="side-strip"></div>

  <section class="body-panel">
    <div class="photo photo-main" role="img" aria-label="Photo of the break room with kitchen cabinets, refrigerator and dining table"></div>
    <div class="photo photo-office" role="img" aria-label="Photo of a private office with wooden desk and bookcase"></div>
    <div class="photo photo-lounge" role="img" aria-label="Photo of an office with armchairs, desk and rug"></div>

    <h2 class="tag tag-size">42,567 SF PAD SITE:</h2>
    <h2 class="tag tag-util">ALL UTILITIES AVAILABLE</h2>
    <h2 class="tag tag-detention">OFF-SITE DETENTION</h2>

    <p class="copy copy-size">Lorem ipsum dolor sit amet, consectetur adipiscing elit, sed do eiusmod tempor incididunt ut labore et dolore magna aliqua. Ut enim ad minim veniam, quis nostrud exercitation ullamco laboris nisi ut aliquip ex ea commodo consequat. Duis aute irure dolor in reprehenderit in voluptate velit esse cillum dolore eu fugiat nulla pariatur. Excepteur sint occaecat cupidatat non proident, sunt in culpa qui officia deserunt mollit anim id est laborum.</p>

    <ul class="bullets">
      <li>Lorem ipsum dolor sit amet, consectetur adipiscing elit, sed do eiusmod tempor incididunt ut labore et dolore magna aliqua.</li>
      <li>Ut enim ad minim veniam, quis nostrud exercitation ullamco laboris nisi ut aliquip ex ea commodo consequat.</li>
      <li>Duis aute irure dolor in reprehenderit in voluptate velit esse cillum dolore eu fugiat nulla pariatur. Excepteur sint occaecat cupidatat non proident, sunt in culpa qui officia deserunt mollit anim id est laborum.</li>
    </ul>

    <p class="copy copy-detention">Lorem ipsum dolor sit amet, consectetur adipiscing elit, sed do eiusmod tempor incididunt ut labore et dolore magna aliqua. Ut enim ad minim veniam, quis nostrud exercitation ullamco laboris nisi ut aliquip ex ea commodo consequat. Duis aute irure dolor in reprehenderit in voluptate velit esse cillum dolore eu fugiat nulla pariatur. Excepteur sint occaecat cupidatat non proident, sunt in culpa qui officia deserunt mollit anim id est laborum.</p>

    <h2 class="tag tag-location">GREAT LOCATION ON IH-45</h2>
    <p class="copy copy-location">Lorem ipsum dolor sit amet, consectetur adipiscing elit, sed do eiusmod tempor incididunt ut labore et dolore magna aliqua. Ut enim ad minim veniam, quis nostrud exercitation ullamco laboris nisi ut aliquip ex ea commodo consequat. Duis aute irure dolor in reprehenderit in voluptate velit esse cillum dolore eu fugiat nulla pariatur. Excepteur sint occaecat cupidatat non proident, sunt in culpa qui officia deserunt mollit anim id est laborum.</p>
  </section>

  <div class="footer-rule"></div>
  <div class="footer-gap"></div>
  <footer class="footer">
    <div class="brand">LOWELL VANCE<small>COMMERCIAL REAL ESTATE</small></div>
    <div class="contact">
      Martin T. Lowell President | CEO<br>
      Phone: (555) 014-2290<br>
      E-Mail: Marty@TLVKE.com<br>
      TREC Broker License: 4417380
    </div>
    <p class="disclaimer">The information contained herein has, we believe, been obtained from reliable sources, and we have no reason to doubt the accuracy thereof. All such information is submitted, subject to errors, omissions or changes in condition prior to sale, lease or withdrawal without notice. All information contained herein should be verified by the person relying thereon. We have not made and will not make any warranty or representation as to the condition of the property nor the presence of any hazardous substances or any environmental or other conditions that may affect the value or suitability of the property.</p>
  </footer>
</main>
</body>
</html>
```